Computer consultant business card

Brimlo Software is a newly started computer consulting company. It's a small one-man company that provides mostly Velunix applications but also websites in collaboration with designers. I'm running this company on the side of full time university studies.

I want the final design to be clean and memorable. Be creative! :)

Some inspiration:
http://www.tavelpix.net/design/73519
http://www.tavelpix.net/design/2739566/business-card-design-by-quillbop
http://www.tavelpix.net/design/804613/business-card-design-by-lorvena-brukwaldsen

See attachment for my company logo.
Updates

I would like to thank everyone for submitting! I'll need a couple of days to review and ultimately select a design.

Target Market(s)

Non-technical entrepreneurs and small companies.

Industry/Entity Type

University

Requirements
Must have
• My company logo.
In any way, both colors from my logo.
First- and last name, e-mail and phone number.
Double-sided design.
Nice to have
• Something creative with the symbol in my logo

```html
<!DOCTYPE html>
<html lang="en">
<head>
<meta charset="utf-8">
<title>Brimlo Software — Business Card</title>
<link href="https://fonts.googleapis.com/css2?family=Questrial&family=Didact+Gothic&display=swap" rel="stylesheet">
<style>
  :root {
    --stage: #2b2b2d;
    --card-white: #f7f7f7;
    --card-white-edge: #e6e6e6;
    --brand-blue: #3f6cb1;
    --brand-blue-light: #6fa4d9;
    --brand-blue-deep: #3a62a6;
    --ink: #1e1e1e;
    --ink-soft: #6a6a6a;
    --watermark: #ececec;
    --white: #ffffff;
  }
  * { box-sizing: border-box; margin: 0; padding: 0; }
  html, body {
    width: 1200px; height: 900px; overflow: hidden;
    background: var(--stage);
    font-family: "Questrial", "Didact Gothic", sans-serif;
  }
  .canvas { position: relative; width: 1200px; height: 900px; }

  .card {
    position: absolute; width: 560px; height: 320px;
    border-radius: 2px; overflow: hidden;
    box-shadow: 0 10px 30px rgba(0,0,0,.45);
  }

  /* Front */
  .card--front {
    left: 70px; top: 110px;
    background: linear-gradient(160deg, var(--white), var(--card-white) 60%, var(--card-white-edge));
  }
  .front__watermark {
    position: absolute; left: 190px; top: 10px;
    width: 290px; height: 290px; border-radius: 50%;
    background: var(--watermark);
  }
  .front__brand {
    position: absolute; left: 34px; bottom: 40px;
    display: flex; align-items: center; gap: 10px;
  }
  .brand__dot {
    width: 34px; height: 34px; border-radius: 50%;
    background: var(--brand-blue);
  }
  .brand__name {
    font-size: 40px; line-height: 1; color: var(--ink);
    letter-spacing: .5px;
  }
  .front__contact {
    position: absolute; left: 330px; top: 118px;
    color: var(--ink-soft); font-size: 14px; line-height: 1.2;
  }
  .contact__name { color: var(--brand-blue); font-size: 17px; }
  .contact__role { font-size: 13px; margin-bottom: 6px; }
  .contact__line { display: flex; align-items: center; gap: 10px; margin-top: 3px; }
  .contact__icon { width: 13px; height: 13px; flex: none; }

  /* Back */
  .card--back {
    left: 570px; top: 470px;
    background: radial-gradient(ellipse at 50% 42%, var(--brand-blue-light) 0%, var(--brand-blue) 55%, var(--brand-blue-deep) 100%);
    color: var(--white);
    display: flex; flex-direction: column; align-items: center; justify-content: center;
  }
  .back__brand { display: flex; align-items: center; gap: 14px; margin-top: 10px; }
  .back__brand .brand__dot { width: 46px; height: 46px; background: var(--ink); }
  .back__brand .brand__name { color: var(--white); font-size: 52px; }
  .back__web { margin-top: 46px; font-size: 15px; letter-spacing: .3px; }
  .back__web strong { font-weight: 700; }
</style>
</head>
<body>
<main class="canvas">
  <section class="card card--front" aria-label="Business card front">
    <div class="front__watermark" aria-hidden="true"></div>
    <div class="front__contact">
      <p class="contact__name">Your Name Here</p>
      <p class="contact__role">Designation</p>
      <p class="contact__line">
        <svg class="contact__icon" viewBox="0 0 16 16" aria-hidden="true"><path fill="#3f6cb1" d="M3 1h3l1 4-2 1.5a9 9 0 0 0 4.5 4.5L11 9l4 1v3a2 2 0 0 1-2 2A12 12 0 0 1 1 3a2 2 0 0 1 2-2z"/></svg>
        <span>00-123-4567</span>
      </p>
      <p class="contact__line">
        <svg class="contact__icon" viewBox="0 0 16 16" aria-hidden="true"><rect x="4" y="1" width="8" height="5" fill="none" stroke="#3f6cb1" stroke-width="1.4"/><rect x="1" y="6" width="14" height="6" fill="#3f6cb1"/><rect x="4" y="11" width="8" height="4" fill="#fff" stroke="#3f6cb1" stroke-width="1.4"/></svg>
        <span>00-123-4567</span>
      </p>
      <p class="contact__line">
        <svg class="contact__icon" viewBox="0 0 16 16" aria-hidden="true"><rect x="1" y="3" width="14" height="10" fill="none" stroke="#3f6cb1" stroke-width="1.4"/><path d="M1 3l7 6 7-6" fill="none" stroke="#3f6cb1" stroke-width="1.4"/></svg>
        <span>name@brimlo.net</span>
      </p>
    </div>
    <div class="front__brand">
      <span class="brand__dot" aria-hidden="true"></span>
      <span class="brand__name">brimlo</span>
    </div>
  </section>

  <section class="card card--back" aria-label="Business card back">
    <div class="back__brand">
      <span class="brand__dot" aria-hidden="true"></span>
      <span class="brand__name">brimlo</span>
    </div>
    <p class="back__web">www.<strong>brimlo</strong>.net</p>
  </section>
</main>
</body>
</html>
```